Business Card

Just need business logo with phone number on it. 0487 312 556
And the following on the bottom of the card.

"Your local plumbing experts".
and emblems for kelpa card, cheque and cash

```html
<!DOCTYPE html>
<html lang="en">
<head>
<meta charset="utf-8">
<title>Ridgeline Plumbing &amp; Drainage – Business Card</title>
<link rel="stylesheet" href="https://fonts.googleapis.com/css2?family=Michroma&family=Roboto:wght@400;500;700&display=swap">
<style>
  :root {
    --backdrop: #d9d9d9;
    --card: #f7f7f5;
    --brand-red: #d0231c;
    --brand-blue: #0a6fbf;
    --white: #ffffff;
    --cheque: #f6ec9a;
    --cheque-edge: #c9b845;
    --cash: #7fb89a;
    --ink: #2b2b2b;
  }
  html, body {
    margin: 0;
    padding: 0;
    width: 1200px;
    height: 902px;
    overflow: hidden;
    background: var(--backdrop);
  }
  .stage {
    position: relative;
    width: 1200px;
    height: 902px;
  }
  .card {
    position: absolute;
    left: 50px;
    top: 131px;
    width: 1100px;
    height: 640px;
    border-radius: 40px;
    overflow: hidden;
    background: var(--card);
    box-shadow: 0 10px 30px rgba(0,0,0,0.25);
  }
  .card-bands {
    position: absolute;
    inset: 0;
  }
  .brand-name {
    position: absolute;
    left: 300px;
    top: 70px;
    width: 620px;
    font-family: "Michroma", sans-serif;
    color: var(--brand-red);
    text-transform: uppercase;
    line-height: 1.15;
  }
  .brand-name .line-main {
    display: block;
    font-size: 58px;
    letter-spacing: 2px;
  }
  .brand-name .line-sub {
    display: block;
    font-size: 25px;
    letter-spacing: 6px;
  }
  .brand-name .line-legal {
    display: block;
    font-size: 13px;
    letter-spacing: 3px;
    margin-top: 6px;
    text-align: right;
  }
  .phone {
    position: absolute;
    left: 250px;
    top: 260px;
    display: flex;
    align-items: center;
    gap: 22px;
  }
  .phone-icon {
    width: 46px;
    height: 46px;
  }
  .phone-number {
    font-family: "Michroma", sans-serif;
    font-size: 60px;
    color: var(--brand-blue);
    letter-spacing: 2px;
    white-space: nowrap;
  }
  .rule {
    position: absolute;
    height: 4px;
    background: var(--brand-red);
    border-radius: 2px;
  }
  .rule-left { left: 240px; top: 350px; width: 90px; }
  .rule-right { left: 820px; top: 410px; width: 90px; }
  .tagline {
    position: absolute;
    left: 360px;
    top: 345px;
    font-family: "Roboto", sans-serif;
    font-size: 32px;
    color: var(--brand-blue);
    white-space: nowrap;
  }
  .payment-label {
    position: absolute;
    left: 40px;
    top: 430px;
    font-family: "Roboto", sans-serif;
    font-size: 32px;
    color: var(--white);
  }
  .payment-methods {
    position: absolute;
    left: 560px;
    top: 505px;
    display: flex;
    align-items: center;
    gap: 26px;
  }
  .method {
    height: 62px;
    display: flex;
    align-items: center;
    justify-content: center;
    border-radius: 6px;
    box-sizing: border-box;
  }
  .method-card {
    width: 96px;
    background: var(--white);
    border: 2px solid var(--brand-blue);
    font-family: "Roboto", sans-serif;
    font-weight: 700;
    font-size: 26px;
    color: var(--brand-blue);
  }
  .method-cheque {
    width: 130px;
    position: relative;
    background: var(--cheque);
    border: 2px solid var(--cheque-edge);
    font-family: "Roboto", sans-serif;
    font-size: 10px;
    font-weight: 700;
    color: var(--ink);
  }
  .method-cheque .cheque-title {
    position: absolute;
    top: 8px;
    left: 52px;
  }
  .method-cheque .cheque-line {
    position: absolute;
    height: 2px;
    background: var(--ink);
  }
  .method-cheque .l1 { left: 12px; top: 14px; width: 30px; }
  .method-cheque .l2 { left: 12px; top: 30px; width: 90px; }
  .method-cheque .l3 { left: 12px; top: 44px; width: 60px; }
  .method-cheque .sig { position: absolute; right: 10px; bottom: 8px; width: 22px; height: 7px; background: var(--ink); }
  .method-cash {
    width: 120px;
    background: var(--cash);
    font-family: "Roboto", sans-serif;
    font-weight: 500;
    font-size: 26px;
    color: var(--white);
  }
</style>
</head>
<body>
<div class="stage">
  <div class="card">
    <svg class="card-bands" width="1100" height="640" viewBox="0 0 1100 640" aria-hidden="true">
      <polygon points="0,400 477,400 300,640 0,640" fill="var(--brand-blue)"/>
      <polygon points="440,450 1100,450 1100,640 300,640" fill="var(--brand-red)"/>
    </svg>

    <div class="brand-name">
      <span class="line-main">Ridgeline</span>
      <span class="line-sub">Plumbing &amp; Drainage</span>
      <span class="line-legal">Pty Ltd</span>
    </div>

    <div class="phone">
      <svg class="phone-icon" viewBox="0 0 46 46" aria-hidden="true">
        <circle cx="23" cy="23" r="20" fill="none" stroke="var(--brand-red)" stroke-width="4"/>
        <path d="M16 13 l5 0 l2 6 l-3 2 q2 5 7 7 l2 -3 l6 2 l0 5 q-1 2 -4 2 q-10 -1 -16 -10 q-3 -5 -1 -11 z" fill="var(--brand-red)"/>
      </svg>
      <span class="phone-number">0487 312 556</span>
    </div>

    <div class="rule rule-left"></div>
    <div class="tagline">Your local plumbing experts</div>
    <div class="rule rule-right"></div>

    <div class="payment-label">Payment made from:</div>

    <div class="payment-methods">
      <div class="method method-card">kelpa</div>
      <div class="method method-cheque">
        <span class="cheque-line l1"></span>
        <span class="cheque-title">CHEQUE</span>
        <span class="cheque-line l2"></span>
        <span class="cheque-line l3"></span>
        <span class="sig"></span>
      </div>
      <div class="method method-cash">CA$H</div>
    </div>
  </div>
</div>
</body>
</html>
```